Business Card Design Project

use new logo uploaded.

any 3d or shadowing is nice.

white or grey background. metallic brushed silver maybe

horizontal landscape layout

Target Market(s)

dermatologist, plastic surgeons, medpas

Industry/Entity Type

Landscape

Font styles to use
Sans Serif
Other font styles liked:
• use logo font

Requirements
Must have
• horizontal landscape layout
Nice to have
• try font in logo or something like arial

```html
<!DOCTYPE html>
<html lang="en">
<head>
<meta charset="utf-8">
<title>Lumera Skin Lasers – Business Card</title>
<link rel="stylesheet" href="https://fonts.googleapis.com/css2?family=Arimo:wght@400;700&display=swap">
<style>
  :root {
    --backdrop: #d9d9db;
    --card-black: #0c0c0d;
    --card-charcoal: #3a3a3c;
    --sheet-white: #f7f8f8;
    --sheet-edge: #dfe2e2;
    --ink: #111111;
    --icon-grey: #9a9da0;
    --silver-light: #e6e6e8;
    --silver-mid: #a9aaad;
    --silver-dark: #6c6d70;
    --brand-ink: #1a1a1c;
  }
  * { box-sizing: border-box; margin: 0; padding: 0; }
  html, body {
    width: 1200px;
    height: 799px;
    overflow: hidden;
    background: var(--backdrop);
  }
  .canvas {
    position: relative;
    width: 1200px;
    height: 799px;
  }
  .business-card {
    position: absolute;
    left: 220px;
    top: 180px;
    width: 760px;
    height: 440px;
    overflow: hidden;
    border-radius: 3px;
    background: linear-gradient(160deg, var(--card-black) 0%, #1d1d1f 40%, var(--card-charcoal) 75%, #505052 100%);
    box-shadow: 0 18px 40px rgba(0,0,0,0.35);
    font-family: "Arimo", Arial, sans-serif;
  }
  .sheet {
    position: absolute;
    background: var(--sheet-white);
    border: 1px solid var(--sheet-edge);
    box-shadow: -6px 8px 16px rgba(0,0,0,0.45);
  }
  .sheet--back {
    left: 150px;
    top: 78px;
    width: 300px;
    height: 240px;
  }
  .sheet--front {
    left: 214px;
    top: 40px;
    width: 400px;
    height: 280px;
    padding: 30px 0 0 44px;
  }
  .contact-icons {
    position: absolute;
    left: 166px;
    top: 104px;
    display: flex;
    flex-direction: column;
    gap: 22px;
  }
  .contact-icons svg { display: block; }
  .holder-name {
    font-size: 23px;
    font-weight: 700;
    color: var(--ink);
    letter-spacing: 0.2px;
  }
  .holder-email {
    margin-top: 22px;
    font-size: 16px;
    font-weight: 400;
    color: var(--ink);
  }
  .holder-phone {
    margin-top: 14px;
    font-size: 17px;
    font-weight: 700;
    color: var(--ink);
  }
  .brand-band {
    position: absolute;
    left: 0;
    right: 0;
    top: 300px;
    bottom: 0;
    background: linear-gradient(180deg, var(--silver-dark) 0%, var(--silver-mid) 18%, var(--silver-light) 45%, var(--silver-mid) 75%, var(--silver-dark) 100%);
    box-shadow: 0 -6px 14px rgba(0,0,0,0.5);
    display: flex;
    flex-direction: column;
    align-items: center;
    padding-top: 28px;
    color: var(--brand-ink);
    font-weight: 400;
  }
  .brand-name {
    font-size: 50px;
    letter-spacing: 6px;
    line-height: 1;
  }
  .brand-line {
    margin-top: 10px;
    font-size: 22px;
    letter-spacing: 5px;
    line-height: 1;
  }
</style>
</head>
<body>
<main class="canvas">
  <article class="business-card">
    <div class="sheet sheet--back"></div>
    <div class="contact-icons" aria-hidden="true">
      <svg class="icon-mail" width="22" height="16" viewBox="0 0 22 16">
        <rect x="1" y="1" width="20" height="14" fill="none" stroke="var(--icon-grey)" stroke-width="1.6"/>
        <path d="M1 1 L11 9 L21 1" fill="none" stroke="var(--icon-grey)" stroke-width="1.6"/>
      </svg>
      <svg class="icon-phone" width="20" height="20" viewBox="0 0 24 24">
        <path d="M6.6 10.8a15.1 15.1 0 0 0 6.6 6.6l2.2-2.2c.3-.3.7-.4 1-.2 1.1.4 2.3.6 3.6.6.6 0 1 .4 1 1V20c0 .6-.4 1-1 1A17 17 0 0 1 3 4c0-.6.4-1 1-1h3.5c.6 0 1 .4 1 1 0 1.3.2 2.5.6 3.6.1.3 0 .7-.2 1z" fill="none" stroke="var(--icon-grey)" stroke-width="1.6"/>
      </svg>
    </div>
    <section class="sheet sheet--front">
      <p class="holder-name">Your Name</p>
      <p class="holder-email">123@lumeramail.com</p>
      <p class="holder-phone">(000) 555-6666</p>
    </section>
    <footer class="brand-band">
      <p class="brand-name">LUMERA</p>
      <p class="brand-line">SKIN LASERS</p>
    </footer>
  </article>
</main>
</body>
</html>
```